Corvane Project Services - Flyer

Project Breif:
I need a single page A4 Capability Statement, which will be used to market our services to prospective clients, both in print and via email PDF.
It needs to look professional and should incorporate the elements I have uploaded into files, these include:
Capability Statement Text
Corvane Services Company Logo
Additional Logo’s (Tools We Use)
Glimmer Bay Pics can be cut into the page
I have included examples of capability statements as a guide to what i am looking for.
Regards
Derek
Engineering Consulting

```html
<!DOCTYPE html>
<html lang="en">
<head>
<meta charset="utf-8">
<title>Corvane Project Services – Capability Statement</title>
<link href="https://fonts.googleapis.com/css2?family=Roboto:wght@400;500&family=Oswald:wght@300;600&family=Michroma&display=swap" rel="stylesheet">
<style>
  :root {
    --sky-panel: #bcdff0;
    --sky-band: #86cbe6;
    --sky-band-edge: #a9daee;
    --sky-accent: #7ec4e2;
    --footer-blue: #7ea9d8;
    --ink: #333b42;
    --ink-soft: #4a5058;
    --brand-navy: #1f2a44;
    --white: #ffffff;
  }
  * { margin: 0; padding: 0; box-sizing: border-box; }
  html, body { width: 849px; height: 1200px; overflow: hidden; background: var(--white); }
  .flyer {
    position: relative; width: 849px; height: 1200px; overflow: hidden;
    background: var(--white); font-family: "Roboto", Arial, sans-serif; color: var(--ink);
  }

  /* hero */
  .hero-photo {
    position: absolute; left: 393px; top: 72px; width: 456px; height: 386px;
    background: linear-gradient(135deg, #c9d6e2 0%, #e7edf3 35%, #f5f7f9 55%, #b8c9d9 80%, #9fb6cb 100%);
  }
  .hero-panel {
    position: absolute; left: 38px; top: 72px; width: 355px; height: 386px;
    background: var(--sky-panel);
  }
  .brand {
    position: absolute; left: 0; top: 22px; width: 431px; text-align: center;
  }
  .brand-mark {
    display: block; width: 92px; height: 92px; margin: 0 auto;
    border-radius: 50%; background: #8a96a6;
  }
  .brand-name {
    margin-top: 30px; font-family: "Oswald", Arial, sans-serif; font-weight: 600;
    font-size: 27px; letter-spacing: 1px; text-transform: uppercase; color: var(--brand-navy);
    line-height: 1.15;
  }
  .tagline {
    position: absolute; left: 38px; top: 268px; width: 355px; text-align: center;
    font-family: "Oswald", Arial, sans-serif; font-weight: 300; font-size: 23px;
    line-height: 34.5px; color: var(--brand-navy); text-transform: uppercase;
  }

  /* intro */
  .intro {
    position: absolute; left: 40px; top: 484px; width: 356px;
    font-size: 17.5px; line-height: 21px; color: var(--ink-soft);
  }
  .intro p { margin-bottom: 20px; }

  .core-title {
    position: absolute; left: 40px; top: 806px;
    font-family: "Michroma", Arial, sans-serif; font-size: 25px; color: var(--sky-accent);
    letter-spacing: 1px; text-transform: uppercase;
  }

  .section-band {
    position: absolute; height: 32px; padding-left: 28px;
    background: linear-gradient(90deg, var(--sky-band) 0%, var(--sky-band) 80%, var(--sky-band-edge) 100%);
    clip-path: polygon(0 0, 93% 0, 100% 100%, 0 100%);
    color: var(--white); font-size: 15px; letter-spacing: 2px; line-height: 32px;
    text-transform: uppercase;
  }
  .band-planning { left: 40px; top: 858px; width: 278px; }
  .band-risk { left: 445px; top: 495px; width: 287px; padding-left: 52px; }
  .band-cost { left: 445px; top: 756px; width: 287px; padding-left: 90px; }

  .service-list {
    position: absolute; list-style: none; font-size: 17px; line-height: 28.5px; color: var(--ink-soft);
  }
  .service-list li { position: relative; padding-left: 17px; }
  .service-list li::before {
    content: ""; position: absolute; left: 0; top: 11px; width: 7px; height: 7px;
    border: 1.5px solid var(--sky-accent); border-radius: 50%;
  }
  .list-planning { left: 55px; top: 914px; }
  .list-risk { left: 465px; top: 549px; }
  .list-cost { left: 465px; top: 809px; }

  /* footer */
  .contact-bar {
    position: absolute; left: 0; top: 1135px; width: 849px; height: 65px;
    background: var(--footer-blue); color: var(--white);
  }
  .contact-name {
    position: absolute; left: 468px; top: 14px;
    font-family: "Oswald", Arial, sans-serif; font-weight: 600; font-size: 14px; letter-spacing: 1px;
  }
  .contact-details {
    position: absolute; left: 468px; top: 41px; font-size: 11px; letter-spacing: 0.6px;
  }
</style>
</head>
<body>
<main class="flyer">
  <div class="hero-photo" role="img" aria-label="Photo of hands reviewing printed project charts and documents with a pen"></div>

  <header class="brand">
    <span class="brand-mark"></span>
    <div class="brand-name">Corvane Project<br>Services</div>
  </header>
  <div class="hero-panel"></div>
  <header class="brand">
    <span class="brand-mark"></span>
    <div class="brand-name">Corvane Project<br>Services</div>
  </header>
  <h1 class="tagline">Leading project control<br>consultancy based in Co Cork<br>Ireland</h1>

  <section class="intro">
    <p>For over 20 years we have been helping our clients to deliver complex projects and programs throughout mainland Europe.</p>
    <p>We are passionate about empower organisations to achieve their objectives, on time and on budget.</p>
    <p>We are continually innovating, evolving and learning, utilize the latest industry tools and techniques to deliver real value to our clients.</p>
    <p>Our goal is to make successful project delivery more achievable and repeatable.</p>
  </section>

  <h2 class="core-title">Core Services</h2>

  <h3 class="section-band band-planning">Planning &amp; Scheduling</h3>
  <ul class="service-list list-planning">
    <li>Tender Planning</li>
    <li>Interactive Planning / Pull Planning</li>
    <li>EPCMV Planning &amp; Scheduling</li>
    <li>Schedule Earned Value Management</li>
    <li>Independent Schedule Quality Assessment</li>
    <li>Schedule Risk Analysis (Monte Carlo)</li>
    <li>Training</li>
  </ul>

  <h3 class="section-band band-risk">Management of Risk</h3>
  <ul class="service-list list-risk">
    <li>Risk Management Policies &amp; Procedures</li>
    <li>Risk Management Strategy</li>
    <li>Risk Registers</li>
    <li>Risk Improvement Planning</li>
    <li>Risk Response and Communication</li>
    <li>Risk Management Training</li>
  </ul>

  <h3 class="section-band band-cost">Cost Control</h3>
  <ul class="service-list list-cost">
    <li>Estimating &amp; Forecasting</li>
    <li>Earned Value Analysis</li>
    <li>Progress Reporting</li>
    <li>Cost Risk Analysis</li>
  </ul>

  <footer class="contact-bar">
    <div class="contact-name">DEREK HALLORY (MANAGING DIRECTOR)</div>
    <div class="contact-details">INFO@CORVANESERVICES.IE &nbsp;|&nbsp; WWW.CORVANESERVICES.IE &nbsp;|&nbsp; +353 (0)870 415 926</div>
  </footer>
</main>
</body>
</html>
```